Dental Office Needs Exciting New Stationary

We need a stationary design that incorporates the logo that we already have and would like to keep the existing color scheme. We need something clean and professional. This is a Endodontic (root canals) office and must represent a dental specialist's office. I need a design for a business card, envelope, and letterhead that all coordinate. I would like the business card to incorporate the information in the business card sample that I am providing. I made the business card design myself but would like to see a better one.

```html
<!DOCTYPE html>
<html lang="en">
<head>
<meta charset="UTF-8">
<title>Harbor Endodontics – Business Card</title>
<link href="https://fonts.googleapis.com/css2?family=Lato:wght@300;400;700&display=swap" rel="stylesheet">
<style>
  :root{
    --bg:#cfd8de;
    --navy:#27356b;
    --grey:#58595d;
    --text:#aab3cc;
    --name:#b9c1d6;
    --accent:#3f8fd9;
    --silver:#c9ccd2;
  }
  html,body{margin:0;padding:0;width:1200px;height:1000px;overflow:hidden;background:var(--bg);}
  body{position:relative;font-family:'Lato',sans-serif;}
  .card{position:absolute;width:480px;height:274px;background:var(--navy);overflow:hidden;
        box-shadow:0 3px 6px rgba(0,0,0,.25);}
  .card--front{left:150px;top:170px;}
  .card--back{left:580px;top:520px;}

  .front-mark{position:absolute;inset:0;display:flex;align-items:center;justify-content:center;gap:10px;}
  .mark-dot{width:14px;height:14px;border-radius:50%;background:var(--accent);}
  .mark-name{font-weight:700;font-size:20px;letter-spacing:3px;color:var(--accent);}

  .swoosh{position:absolute;left:0;top:0;width:480px;height:274px;}

  .brand{position:absolute;left:30px;top:108px;display:flex;align-items:center;gap:9px;}
  .brand .mark-dot{width:12px;height:12px;}
  .brand-name{font-weight:700;font-size:13px;letter-spacing:1.5px;color:var(--accent);line-height:1.25;}

  .info{position:absolute;left:200px;top:38px;color:var(--text);}
  .doctors{font-weight:300;font-size:15px;color:var(--name);line-height:1.3;margin:0 0 12px;}
  .contact{list-style:none;margin:0;padding:0;font-size:9.5px;font-weight:400;line-height:1.75;}
  .contact li{display:flex;align-items:center;gap:6px;}
  .contact svg{width:8px;height:8px;fill:var(--accent);flex:none;}
  .contact .gap{margin-top:6px;}

  .corner-mark{position:absolute;right:22px;top:150px;font-weight:700;font-size:12px;letter-spacing:2px;color:var(--silver);}
</style>
</head>
<body>

<section class="card card--front">
  <div class="front-mark">
    <span class="mark-dot"></span>
    <span class="mark-name">HARBOR</span>
  </div>
</section>

<section class="card card--back">
  <svg class="swoosh" viewBox="0 0 480 274" aria-hidden="true">
    <path d="M0,274 C170,262 360,228 480,160 L480,274 Z" fill="var(--grey)"/>
  </svg>

  <div class="brand">
    <span class="mark-dot"></span>
    <span class="brand-name">HARBOR<br>ENDODONTICS</span>
  </div>

  <div class="info">
    <p class="doctors">Daniel R. Whitmore DDS MS<br>Marco L. Ferreira DDS</p>
    <ul class="contact">
      <li><svg viewBox="0 0 10 10"><path d="M5 0a3.5 3.5 0 0 0-3.5 3.5C1.5 6 5 10 5 10s3.5-4 3.5-6.5A3.5 3.5 0 0 0 5 0zm0 5a1.4 1.4 0 1 1 0-2.8A1.4 1.4 0 0 1 5 5z"/></svg>2140 Elm Street, Riverton, Ca 95000</li>
      <li><svg viewBox="0 0 10 10"><path d="M2 0l2 2.5-1.2 1.3a6 6 0 0 0 3.4 3.4L7.5 6 10 8l-1.5 2C4 10 0 6 0 1.5z"/></svg>555.201.4470</li>
      <li><svg viewBox="0 0 10 10"><rect x="0" y="2" width="10" height="6"/></svg>555.201.4471</li>
      <li class="gap"><svg viewBox="0 0 10 10"><path d="M5 0a3.5 3.5 0 0 0-3.5 3.5C1.5 6 5 10 5 10s3.5-4 3.5-6.5A3.5 3.5 0 0 0 5 0zm0 5a1.4 1.4 0 1 1 0-2.8A1.4 1.4 0 0 1 5 5z"/></svg>815 Oak Av. Suite #3, Lakeview, Ca 95010</li>
      <li><svg viewBox="0 0 10 10"><path d="M2 0l2 2.5-1.2 1.3a6 6 0 0 0 3.4 3.4L7.5 6 10 8l-1.5 2C4 10 0 6 0 1.5z"/></svg>555.310.8820</li>
      <li><svg viewBox="0 0 10 10"><rect x="0" y="2" width="10" height="6"/></svg>555.310.8821</li>
      <li class="gap"><svg viewBox="0 0 10 10"><circle cx="5" cy="5" r="5"/></svg>www.harborendo.com</li>
    </ul>
  </div>

  <span class="corner-mark">HARBOR</span>
</section>

</body>
</html>
```